serious, thorough, light and simple - that's my advice and mediations

My business card should combine my logo (uploaded file) and my homepage (https://feltra-mediation.plavosite.com).

Contact Information for Business Card

Name: Sabine Feltra di Olvesi
Phone: 079 417 68 92
mail: sfeltra@plovix.ch
web: www.feltra-di-olvesi.ch

```html
<!DOCTYPE html>
<html lang="de">
<head>
<meta charset="utf-8">
<title>Visitenkarte – Sabine Feltra di Olvesi</title>
<link rel="stylesheet" href="https://fonts.googleapis.com/css2?family=Roboto:wght@400;500;700&display=swap">
<style>
  :root {
    --bg: #eeeeee;
    --card-white: #ffffff;
    --green: #0f6b3a;
    --blue: #1b4784;
    --navy: #1f3f88;
    --gold: #a77a3f;
    --text-grey: #3a3a3a;
    --white: #ffffff;
  }
  html, body {
    margin: 0;
    padding: 0;
    width: 1200px;
    height: 800px;
    overflow: hidden;
    background: var(--bg);
    font-family: "Roboto", Arial, sans-serif;
  }
  .canvas {
    position: relative;
    width: 1200px;
    height: 800px;
  }
  .card {
    position: absolute;
    width: 570px;
    height: 330px;
    box-sizing: border-box;
  }
  /* Back side: contact details */
  .card--contact {
    left: 476px;
    top: 32px;
    background: var(--card-white);
  }
  .brand {
    display: flex;
    align-items: center;
    gap: 10px;
    font-weight: 500;
    white-space: nowrap;
  }
  .brand__dot {
    flex: none;
    border-radius: 50%;
  }
  .card--contact .brand {
    position: absolute;
    left: 42px;
    top: 62px;
    font-size: 30px;
    color: var(--gold);
  }
  .card--contact .brand__dot {
    width: 18px;
    height: 18px;
    background: var(--green);
  }
  .name-bar {
    position: absolute;
    left: 0;
    top: 193px;
    width: 19px;
    height: 11px;
    background: var(--navy);
  }
  .person-name {
    position: absolute;
    left: 41px;
    top: 186px;
    margin: 0;
    font-size: 17px;
    font-weight: 700;
    letter-spacing: 0.3px;
    text-transform: uppercase;
    color: var(--green);
  }
  .contact-list {
    position: absolute;
    left: 41px;
    top: 226px;
    margin: 0;
    padding: 0;
    list-style: none;
  }
  .contact-list li {
    display: flex;
    align-items: center;
    gap: 8px;
    height: 20px;
    font-size: 16px;
    color: var(--text-grey);
  }
  .contact-list svg {
    width: 13px;
    height: 13px;
    fill: var(--gold);
    flex: none;
  }
  /* Front side: brand on gradient */
  .card--brand {
    left: 170px;
    top: 404px;
    background: linear-gradient(180deg, var(--green) 0%, var(--blue) 100%);
    display: flex;
    align-items: center;
    justify-content: center;
  }
  .card--brand .brand {
    font-size: 46px;
    color: var(--white);
  }
  .card--brand .brand__dot {
    width: 26px;
    height: 26px;
    border: 3px solid var(--white);
    box-sizing: border-box;
  }
</style>
</head>
<body>
<main class="canvas">

  <section class="card card--contact" aria-label="Kartenrückseite mit Kontaktdaten">
    <div class="brand">
      <span class="brand__dot"></span>
      <span class="brand__name">Wege im Dialog</span>
    </div>

    <span class="name-bar"></span>
    <h1 class="person-name">Sabine Feltra di Olvesi</h1>

    <ul class="contact-list">
      <li>
        <svg viewBox="0 0 16 16" aria-hidden="true"><path d="M2 6c0-2 2-3 6-3s6 1 6 3v1h-3V5.5C10 5 9 5 8 5s-2 0-3 .5V7H2z"/><path d="M4 8h8l1.5 5h-11z"/></svg>
        <span>079 417 68 92</span>
      </li>
      <li>
        <svg viewBox="0 0 16 16" aria-hidden="true"><path d="M1 3h14v10H1z M2 4l6 5 6-5" fill-rule="evenodd"/></svg>
        <span>sfeltra@plovix.ch</span>
      </li>
      <li>
        <svg viewBox="0 0 16 16" aria-hidden="true"><circle cx="8" cy="8" r="7"/></svg>
        <span>www.feltra-di-olvesi.ch</span>
      </li>
    </ul>
  </section>

  <section class="card card--brand" aria-label="Kartenvorderseite">
    <div class="brand">
      <span class="brand__dot"></span>
      <span class="brand__name">Wege im Dialog</span>
    </div>
  </section>

</main>
</body>
</html>
```